LADIES' HORIZON ALLIANCE

Design a website for a membership based organization focusing on entrepreneurship, women's issues and global news regarding commerce.
Also, want a news daily tie in to site, and social media outlets.
I want the colors in strong blue, deep or metallic gold and cream/white like logo which will be provided. I want logo altered with globe to replace small sphere in the design.
Also, board members page that should be redesigned. Might need extra coding.
PLEASE SEE http://ladieshorizonalliance.example DIDN'T LIKE THIS LAY OUT AT ALL TOO MUCH WHITE AND NOT ENOUGH IMPACT. WANT TO DRAW MEMBERS.

PLEASE SEE http://www.tqrb-example.com/Index.cfm BUT THIS IS WAY TO BUSY BUT I LIKE THE SLIDING.

SEE OUR TWITTER ACCOUNT FOR INSIGHT. @LADIESHORALL

Reason: Happy Holidays. The board approving the design will be out on season time vacation until Jan. 2. Please make any edits requested from designer already submitting layouts. Thank you, Delphine

Target Market(s)

GLOBAL BUSINESS WOMEN AND ENTREPRENEURS AGES 20-65

Industry/Entity Type

Media

Number of Pages Required

4 page

Font styles to use
Other font styles liked:
• Baskerville or something similar

Colors
fbed22
3377b5
9bcb3c

Requirements
Must have
• Show diversity of ethnicities if using stock photos. Vibrant and inviting site, MUST JOIN or Be part of this organization. Luxury style
• THIS IS A FOR PROFIT WEBSITE.
• Membership Fees:
• Annual Fee $250
• For an additional fee of $150 you can grow your visibility and voice through our Ladies' Horizon Alliance Newsletter and Speaker's Bureau (LHANSB).
• LHA Speaker's Bureau will support your personal, business and organizations' objectives and to give you greater visibility and voice as an authority world leader or business visionary in your field of service.
• LHASB realizes that so many worthy leaders' in diverse fields of service are never allowed to be heard. If you feel you are a dynamic speaker, run a worthwhile business or organization and whose wisdom and success can be of service of others sign up today and be part of the LHASB!
• Student Membership
• Discounted student memberships are also available. Students have access to selected group forums, as well as selected groups of members that provide mentoring. Mentoring helps continue the member's legacy and creates a well spring of future leaders. Student membership fees cost just $75 a year.
• Contact us to help promote you and other women's vision throughout the world.
• Join LHA Now!
• CAN YOU PROVIDE A HEADLINE WITHOUT WOMEN SEE TWITTER ACCOUNT.
Nice to have
• Nice headline and well position tabs.
• Home
• Join LHA Now
• Memberships
• LHA Team Leadership
• About Us
• Contact
• LHA is an Effective Women's Alliance for You!
• New Member - Women's Organization
• 20% Discount- Offer Valid on Your Membership Fee When You Join before 1/30/2105
• Memberships
• LHA Leadership
• At Ladies' Horizon Alliance, we offer the opportunity to connect with women throughout the globe. Join these trailblazers to shorten your path to success and camaraderie.
• Who We Are
• Ladies' Horizon Alliance is an online women's initiative that promotes your business and visions through social engagement. We are here to help you form strategic partnerships with like-minded women around the world. End your solo journey by becoming a member of LHA.
• LHA also features a forum to promote the services, campaigns, and social activism by our members.
• LHA is about women helping other women. Contact us for more information.
• Learn More about Ladies' Horizon Alliance
• Contact us for more information in regards to LHA membership and how to get involved.
• SHARE THIS PAGE:
• twitter, fb, instagram, etc.

```html
<!DOCTYPE html>
<html lang="en">
<head>
<meta charset="utf-8">
<title>Ladies' Horizon Alliance</title>
<link href="https://fonts.googleapis.com/css2?family=Lato:wght@400;700;900&family=Open+Sans:wght@300;400&display=swap" rel="stylesheet">
<style>
:root{
  --gold:#f9be22;
  --blue:#0f6fb8;
  --cream:#efeee4;
  --ink:#333;
  --body:#444;
  --footer:#3f3f3f;
  --footer-text:#d6d6d6;
  --grey-btn:#9a9a9a;
}
*{box-sizing:border-box;margin:0;padding:0}
html,body{width:1009px;height:1200px;overflow:hidden;background:#fff}
body{position:relative;font-family:'Lato',sans-serif;color:var(--body)}
.abs{position:absolute}
.top-strip{left:0;top:0;width:1009px;height:3px;background:var(--gold)}
.header{left:0;top:3px;width:1009px;height:69px;border-bottom:2px solid #b5b5b5;background:#fff}
.brand{display:flex;align-items:center;gap:7px}
.brand-dot{width:16px;height:16px;border-radius:50%;background:var(--blue)}
.brand-name{font-size:14px;font-weight:700;color:var(--ink);letter-spacing:-.2px}
.nav{left:435px;display:flex;align-items:center}
.nav a{font-size:11px;color:#333;text-decoration:none;padding:0 13px;height:26px;line-height:26px;display:block;text-transform:uppercase}
.nav a.active{background:var(--gold);color:#fff;border-radius:2px;padding:0 8px;margin-right:6px}
.hero-photo{left:447px;top:72px;width:408px;height:446px;background:linear-gradient(180deg,#8a5a42 0%,#b9876d 35%,#7a5566 65%,#3c2b45 100%)}
.hero-box{left:116px;top:209px;width:235px;height:224px;background:var(--gold);text-align:center;padding-top:45px}
.hero-box h1{font-size:17px;font-weight:900;color:#fff;line-height:19px;text-transform:uppercase}
.hero-box p{font-size:10.5px;color:#5a4410;line-height:18.5px;margin:8px 28px 0}
.hero-btn{display:inline-block;margin-top:14px;background:var(--blue);color:#fff;font-size:10.5px;font-weight:700;padding:0 11px;height:30px;line-height:30px;border-radius:2px}
.arrow{top:277px;width:48px;height:38px;border-radius:2px;display:flex;align-items:center;justify-content:center}
.arrow.prev{left:35px;background:var(--grey-btn)}
.arrow.next{left:928px;background:var(--blue)}
.features{left:0;top:518px;width:1009px;height:209px;background:var(--cream)}
.bar{top:509px;height:9px;width:184px}
.bar.gold{background:var(--gold)}.bar.blue{background:var(--blue)}
.feature{top:487px;width:200px;text-align:center}
.feature .badge{width:100px;height:50px;border-radius:50px 50px 0 0;background:var(--cream);margin:0 auto;display:flex;justify-content:center;padding-top:14px}
.feature h2{font-size:18px;font-weight:700;color:var(--ink);margin-top:7px}
.feature p{font-size:10.5px;line-height:18.5px;color:#444;margin-top:15px;padding:0 18px}
.feature .more{display:inline-block;margin-top:10px;width:57px;height:29px;line-height:29px;border-radius:2px;font-size:13px;font-weight:700}
.more.gold{background:var(--gold);color:#333}.more.blue{background:var(--blue);color:#fff}
.section-title{display:flex;align-items:center;gap:6px;font-size:22px;font-weight:700;color:var(--blue);border-bottom:1px solid #888;padding-bottom:3px}
.about-text{left:94px;top:811px;width:328px;font-size:11px;line-height:18.8px;color:#333;text-align:justify}
.board-card{left:472px;top:808px;width:235px;height:145px;border-radius:3px;background:linear-gradient(120deg,#1f4a4a,#2d3a32 45%,#7a3a1e 80%,#8d2e1a)}
.board-photo{left:49px;top:21px;width:136px;height:89px;border:2px solid #8c6a1c;background:linear-gradient(180deg,#c9a44a,#d8bd86 60%,#8a98b4)}
.board-arrow{top:59px;width:26px;height:26px;background:rgba(0,0,0,.35);border-radius:2px;display:flex;align-items:center;justify-content:center}
.board-name{left:0;width:100%;top:112px;text-align:center;color:#fff;font-style:italic}
.board-name b{display:block;font-size:13px;font-weight:400;line-height:15px}
.board-name span{display:block;font-size:10px;line-height:13px;color:#ddd}
.news-item{left:739px;width:160px;display:flex;gap:6px}
.date{width:32px;height:28px;border-radius:3px;background:linear-gradient(135deg,var(--blue) 50%,#d8c25a 50%);color:#fff;font-size:10px;line-height:11px;padding:2px 3px;position:relative;flex:none}
.date i{position:absolute;right:3px;bottom:2px;font-style:normal;color:var(--blue);background:#f5e9a8;padding:0 1px}
.news-item h3{font-size:11px;font-weight:400;color:#333;line-height:18.5px}
.news-item p{font-size:9.5px;color:#555;line-height:14.5px;margin-top:2px;padding-left:2px;width:120px}
.news-item p a{color:var(--blue);text-decoration:underline;margin-left:8px}
.footer{left:0;top:1003px;width:1009px;height:197px;background:var(--footer);font-family:'Open Sans',sans-serif;color:var(--footer-text)}
.f-title{font-size:21px;font-weight:300;color:#fff;border-bottom:1px solid #ccc;padding-bottom:1px;display:inline-block}
.f-addr{font-size:11px;line-height:18.8px}
.f-divider{left:237px;top:58px;width:1px;height:74px;background:#bbb}
.f-contact{display:flex;align-items:center;gap:9px;font-size:13.5px;white-space:nowrap}
.f-links a{display:block;font-size:11px;line-height:18.8px;color:var(--footer-text);text-decoration:none}
.social{display:flex;gap:3px}
.social span{width:24px;height:24px;border-radius:50%;background:#cfcfcf}
</style>
</head>
<body>
<div class="abs top-strip"></div>
<header class="abs header">
  <div class="abs brand" style="top:22px;left:104px"><span class="brand-dot"></span><span class="brand-name">Ladies' Horizon Alliance</span></div>
  <nav class="abs nav" style="top:22px">
    <a class="active">Home</a><a>About</a><a>Service</a><a>Who we are</a><a>Memberships</a><a>Contact us</a>
  </nav>
</header>

<div class="abs hero-photo" role="img" aria-label="Photograph of a smiling member of the alliance"></div>
<div class="abs hero-box">
  <h1>Ladies' Horizon<br>Alliance</h1>
  <p>It is a long established fact that a reader will be distracted by the readable content of a page when l</p>
  <span class="hero-btn">MEMBERSHIP</span>
</div>
<div class="abs arrow prev"><svg width="18" height="16" viewBox="0 0 18 16"><path d="M9 2 3 8l6 6M16 2l-6 6 6 6" fill="none" stroke="#fff" stroke-width="2"/></svg></div>
<div class="abs arrow next"><svg width="18" height="16" viewBox="0 0 18 16"><path d="M2 2l6 6-6 6M9 2l6 6-6 6" fill="none" stroke="#fff" stroke-width="2"/></svg></div>

<section class="abs features"></section>
<div class="abs bar gold" style="left:104px"></div>
<div class="abs bar blue" style="left:310px"></div>
<div class="abs bar gold" style="left:515px"></div>
<div class="abs bar blue" style="left:721px"></div>

<div class="abs feature" style="left:95px">
  <div class="badge"><svg width="40" height="30" viewBox="0 0 40 30"><path d="M4 8l8 8 8-13 8 13 8-8-3 16H7z" fill="#f9be22"/><rect x="7" y="26" width="26" height="4" fill="#f9be22"/></svg></div>
  <h2>Leadership</h2>
  <p>a significant majority of which are women of color – live in poverty. This situation is cultivated by the marginalization</p>
  <span class="more gold">More</span>
</div>
<div class="abs feature" style="left:301px">
  <div class="badge"><svg width="44" height="38" viewBox="0 0 44 38"><circle cx="22" cy="16" r="13" fill="none" stroke="#0f6fb8" stroke-width="3" stroke-dasharray="5 3"/><rect x="4" y="18" width="36" height="8" rx="2" fill="#0f6fb8"/><rect x="8" y="28" width="4" height="8" fill="#0f6fb8"/><rect x="32" y="28" width="4" height="8" fill="#0f6fb8"/><rect x="16" y="10" width="12" height="8" fill="#0f6fb8"/></svg></div>
  <h2>Leadership</h2>
  <p>a significant majority of which are women of color – live in poverty. This situation is cultivated by the marginalization</p>
  <span class="more blue">More</span>
</div>
<div class="abs feature" style="left:507px">
  <div class="badge"><svg width="36" height="36" viewBox="0 0 36 36"><circle cx="18" cy="18" r="15" fill="none" stroke="#f9be22" stroke-width="3"/><circle cx="18" cy="18" r="7" fill="none" stroke="#f9be22" stroke-width="3"/><path d="M18 0v10M18 26v10M0 18h10M26 18h10" stroke="#f9be22" stroke-width="3"/></svg></div>
  <h2>Leadership</h2>
  <p>a significant majority of which are women of color – live in poverty. This situation is cultivated by the marginalization</p>
  <span class="more gold">More</span>
</div>
<div class="abs feature" style="left:712px">
  <div class="badge"><svg width="48" height="30" viewBox="0 0 48 30"><path d="M2 15Q24-8 46 15Q24 38 2 15z" fill="#0f6fb8"/><circle cx="24" cy="15" r="8" fill="#fff"/><circle cx="24" cy="15" r="5" fill="#0f6fb8"/></svg></div>
  <h2>Leadership</h2>
  <p>a significant majority of which are women of color – live in poverty. This situation is cultivated by the marginalization</p>
  <span class="more blue">More</span>
</div>

<h2 class="abs section-title" style="left:97px;top:766px;width:260px"><svg width="24" height="20" viewBox="0 0 24 20"><path d="M2 19C6 6 14 2 23 1 21 12 14 17 6 15" fill="#0f6fb8"/></svg>About us</h2>
<p class="abs about-text">It is a long established fact that a reader will be distracted by the readable content of a page when looking at its layout. The point of using Lorem Ipsum is that it has a more-or-less normal distribu-tion of letters, as opposed to using 'Content here, content here', making it look like readable English. Many desktop publishing packages and web page editors now use Lorem ,</p>

<h2 class="abs section-title" style="left:459px;top:765px;width:260px"><svg width="24" height="20" viewBox="0 0 24 20"><circle cx="12" cy="5" r="4" fill="#0f6fb8"/><circle cx="4" cy="7" r="3" fill="#0f6fb8"/><circle cx="20" cy="7" r="3" fill="#0f6fb8"/><path d="M5 19q0-9 7-9t7 9zM0 17q0-6 4-6t4 4v2zM24 17q0-6-4-6t-4 4v2z" fill="#0f6fb8"/></svg>Bord Members</h2>
<div class="abs board-card">
  <div class="abs board-photo" role="img" aria-label="Portrait of the founder and president"></div>
  <div class="abs board-arrow" style="left:9px"><svg width="12" height="12" viewBox="0 0 12 12"><path d="M6 1 1 6l5 5M11 1 6 6l5 5" fill="none" stroke="#fff" stroke-width="1.6"/></svg></div>
  <div class="abs board-arrow" style="left:191px"><svg width="12" height="12" viewBox="0 0 12 12"><path d="M1 1l5 5-5 5M6 1l5 5-5 5" fill="none" stroke="#fff" stroke-width="1.6"/></svg></div>
  <div class="abs board-name"><b>Delphine Marlowe</b><span>LHA Founder and President</span></div>
</div>

<h2 class="abs section-title" style="left:739px;top:764px;width:153px"><svg width="20" height="20" viewBox="0 0 20 20"><circle cx="3" cy="17" r="2.5" fill="#0f6fb8"/><path d="M1 9a10 10 0 0 1 10 10M1 2a17 17 0 0 1 17 17" fill="none" stroke="#0f6fb8" stroke-width="3"/></svg>&nbsp;Latest News</h2>
<div class="abs news-item" style="top:810px">
  <div class="date">Mar<i>03</i></div>
  <div><h3>Lorem ipsum eturadipcin praesent vesint</h3><p>Anbun molestie nonuyhe sit variusm<a>More</a></p></div>
</div>
<div class="abs news-item" style="top:887px">
  <div class="date">Mar<i>05</i></div>
  <div><h3>Lorem ipsum eturadipcin praesent vesint</h3><p>Anbun molestie nonuyhe sit variusm<a>More</a></p></div>
</div>

<footer class="abs footer">
  <div class="abs" style="left:104px;top:16px"><h3 class="f-title">contact us</h3></div>
  <p class="abs f-addr" style="left:105px;top:59px">Home Office:<br>480 Harbor Crest Avenue<br>Suite 1200<br>Coral Bay, FL 30001</p>
  <div class="abs f-divider"></div>
  <p class="abs f-addr" style="left:258px;top:55px">Other Location (s):<br>72 Linden Row N.W.<br>Suite 410<br>Easton, DC 20090</p>
  <div class="abs f-contact" style="left:398px;top:57px"><svg width="18" height="18" viewBox="0 0 18 18"><rect width="18" height="18" rx="3" fill="#ccc"/><path d="M5 4l2 0 1 3-1.5 1q1 2.5 3.5 3.5l1-1.5 3 1v2q-6 1-9-6z" fill="#3f3f3f"/></svg>info@lha.example</div>
  <div class="abs f-contact" style="left:398px;top:93px"><svg width="20" height="14" viewBox="0 0 20 14"><rect width="20" height="14" rx="1" fill="#ccc"/><path d="M1 1l9 7 9-7" fill="none" stroke="#3f3f3f" stroke-width="1.5"/></svg>555-014-2290</div>
  <div class="abs" style="left:557px;top:16px"><h3 class="f-title">Quick Links</h3></div>
  <nav class="abs f-links" style="left:560px;top:56px"><a>HOME</a><a>ABOUT</a><a>SERVICE</a><a>WHO WE ARE</a><a>MEMBERSHIPS</a><a>CONTACT US</a></nav>
  <div class="abs" style="left:747px;top:15px"><h3 class="f-title">Follow us</h3></div>
  <div class="abs social" style="left:747px;top:60px"><span></span><span></span><span></span><span></span></div>
</footer>
</body>
</html>
```